Tri-fold Brochure design for Circadian Rhythm Syndrome

HI I want to have circadian rhythm sleep disorder tri-fold brochure template.

I welcome anyone who can do the drawing. Character drawing.
But you can use the below files if you cannot do drawing.

Sleep Rhythm Concept design is welcomed.

I uploaded the tri-fold template here, please use this template.
https://www.stowlyn.com/s/q83pt7fj2xrm61zd/tri-fold_template.ai?dl=0

You can use below file but because all the files below are inconsistent. I welcome you use your own drawings.
https://www.stowlyn.com/sh/v7ndqwrt4ephg29/ZZQ41pM73hfkwR2-bb8nRTqLe?dl=0

You can see below to know what type of brochure we like.
https://www.stowlyn.com/sh/91tq57wibnceyz6/ZZQpN6X42vjrd8hwWkuYLsM-c?dl=0

Sentence you can use here but not need to strictly follow this sentence.
https://www.velnomarsh.org/circadian-rhythm

Circadian rhythm disorder is a sleep rhythm disorder, People become this disorder because of the staying up late bad habit or some people has genetic problem and cannot sleep at night but sleepy daytime.

There are 6 different circadian rhythm disorders.
Jet Lag Disorder:
Shift Work Disorder:
Advanced Sleep Phase Disorder:
Delayed Sleep Phase Disorder:
Non-24 Hour Sleep Wake Disorder:
Irregular Sleep-Wake Rhythm Disorder:

================================

I have done similar contest in the past.
https://www.gigmartoza.com.au/contest/Make-a-Trifold-Brochure-for-Sleep-Disorder-5283917/entries

Your can see what I like and what I do not like from above contest.

I welcome your entry!

```html
<!DOCTYPE html>
<html lang="en">
<head>
<meta charset="utf-8">
<title>Circadian Rhythm Disorder – Tri-fold Brochure</title>
<link rel="stylesheet" href="https://fonts.googleapis.com/css2?family=Rubik:wght@300;400;500;700&family=Open+Sans:wght@400&display=swap">
<style>
  :root{
    --backdrop:#65739a;
    --lavender:#b4bde0;
    --lavender-soft:#d9dcef;
    --blush:#f1c9cc;
    --blush-deep:#e8a9ae;
    --paper:#ffffff;
    --ink:#2d3343;
    --teal:#3c7d98;
    --coral:#d9837c;
    --navy:#3f4b7a;
  }
  *{margin:0;padding:0;box-sizing:border-box}
  html,body{width:1200px;height:1200px;overflow:hidden;background:var(--backdrop)}
  .brochure{position:absolute;left:59px;top:181px;width:1078px;height:767px;overflow:hidden;background:var(--paper)}
  .brochure-bg{position:absolute;inset:0}
  .panel{position:absolute;top:0;width:359px;height:767px}
  .panel--inside-left{left:0}
  .panel--inside-middle{left:359px}
  .panel--cover{left:718px;width:360px}
  .text-block{position:absolute;font-family:"Open Sans",Arial,sans-serif;color:var(--ink);font-size:9.4px;line-height:1.36;text-align:justify}
  .tips-heading{position:absolute;left:41px;top:40px;font-family:"Rubik",Arial,sans-serif;font-weight:300;font-size:29px;line-height:1.12;color:var(--ink)}
  .tips-heading strong{font-weight:500;color:var(--teal)}
  .tips-body{left:41px;top:163px;width:293px}
  .tips-body p+p{margin-top:7px}
  .kicker{position:absolute;left:29px;top:57px;font-family:"Rubik",Arial,sans-serif;font-size:17px;color:var(--ink)}
  .define-title{position:absolute;left:29px;top:83px;font-family:"Rubik",Arial,sans-serif;font-weight:500;font-size:26px;line-height:1.05;color:var(--ink);letter-spacing:.3px}
  .define-title span{color:var(--teal)}
  .define-body{left:29px;top:166px;width:322px;text-align:left}
  .art{position:absolute}
  .art--tips{left:12px;top:400px;width:336px;height:255px}
  .art--sleeper{left:26px;top:240px;width:300px;height:208px}
  .subhead{position:absolute;left:100px;top:482px;font-family:"Rubik",Arial,sans-serif;font-weight:300;font-size:22px;color:var(--coral)}
  .clock-icon{position:absolute;left:23px;top:511px;width:58px;height:58px}
  .jetlag-body{left:100px;top:518px;width:252px;font-size:9.8px;line-height:1.33;text-align:justify}
  .filler-body{left:29px;top:592px;width:322px;line-height:1.3}
  .cover-title{position:absolute;right:47px;top:117px;text-align:right;font-family:"Rubik",Arial,sans-serif;font-weight:500;font-size:33px;line-height:1.12;color:var(--ink);letter-spacing:.6px}
  .cover-title span{color:var(--teal)}
  .art--clock{left:2px;top:250px;width:356px;height:298px}
  .art--alarm{left:55px;top:600px;width:248px;height:128px}
</style>
</head>
<body>
<div class="brochure">
  <svg class="brochure-bg" width="1078" height="767" viewBox="0 0 1078 767" aria-hidden="true">
    <defs>
      <linearGradient id="insideSky" x1="0" y1="0" x2="0" y2="1">
        <stop offset="0" stop-color="#b4bde0"/>
        <stop offset=".5" stop-color="#d9dcef"/>
        <stop offset="1" stop-color="#ffffff"/>
      </linearGradient>
      <linearGradient id="coverSky" x1="0" y1="0" x2="0" y2="1">
        <stop offset="0" stop-color="#b4bde0"/>
        <stop offset="1" stop-color="#d9dcef"/>
      </linearGradient>
      <linearGradient id="foldShade" x1="0" y1="0" x2="1" y2="0">
        <stop offset="0" stop-color="#8f98c2" stop-opacity=".25"/>
        <stop offset=".3" stop-color="#ffffff" stop-opacity="0"/>
      </linearGradient>
    </defs>
    <rect x="0" y="0" width="718" height="767" fill="url(#insideSky)"/>
    <path d="M0 290 C120 250 240 320 360 295 C480 270 600 320 718 295 L718 470 L0 470Z" fill="#f1c9cc" opacity=".8"/>
    <path d="M0 330 C150 300 260 375 380 340 C500 305 620 355 718 330 L718 767 L0 767Z" fill="#ffffff" opacity=".92"/>
    <path d="M0 650 C140 610 280 700 420 670 C560 640 640 690 718 665 L718 767 L0 767Z" fill="#c8cbe6"/>
    <path d="M0 690 C160 660 300 730 460 705 C580 690 660 715 718 700 L718 767 L0 767Z" fill="#b4bde0"/>
    <rect x="359" y="0" width="359" height="767" fill="url(#foldShade)"/>
    <rect x="718" y="0" width="360" height="767" fill="#ffffff"/>
    <path d="M718 0 L1078 0 L1078 45 C980 40 900 60 840 110 C800 145 760 160 718 165Z" fill="url(#coverSky)"/>
    <path d="M718 700 C820 680 940 705 1078 685 L1078 767 L718 767Z" fill="#f1c9cc" opacity=".8"/>
    <path d="M718 730 C840 715 960 735 1078 722 L1078 767 L718 767Z" fill="#d9dcef"/>
    <line x1="359" y1="0" x2="359" y2="767" stroke="#9aa3c8" stroke-opacity=".35"/>
    <line x1="718" y1="0" x2="718" y2="767" stroke="#9aa3c8" stroke-opacity=".35"/>
  </svg>

  <section class="panel panel--inside-left">
    <h2 class="tips-heading">How To Maintain<br>A <strong>Healthy<br>Circadian Rhythm</strong></h2>
    <div class="text-block tips-body">
      <p>Lorem ipsum dolor sit amet, consectetuer adipiscing elit, sed diam nonummy nibh euismod tincidunt ut laoreet dolore magna aliquam erat volutpat. Ut wisi enim ad minim veniam, quis nostrud exerci tation ullamcorper suscipit lobortis nisl ut aliquip ex ea commodo consequat.</p>
      <p>Duis autem vel eum iriure dolor in hendrerit in vulputate velit esse molestie consequat, vel illum dolore eu feugiat nulla facilisis at vero eros et accumsan et iusto odio dignissim qui blandit praesent luptatum zzril delenit augue duis dolore te feugait nulla facilisi.</p>
    </div>
    <svg class="art art--tips" viewBox="0 0 336 255" role="img" aria-label="Illustration: two small figures beside a giant sleep mask, a clock ringed with stars and floating Z letters">
      <defs>
        <linearGradient id="tipsFill" x1="0" y1="0" x2="1" y2="1">
          <stop offset="0" stop-color="#e9c3cc"/>
          <stop offset="1" stop-color="#b4bde0"/>
        </linearGradient>
      </defs>
      <path d="M30 200 C10 160 40 90 110 70 C150 20 230 20 260 60 C320 70 340 140 310 190 C300 230 250 245 170 240 C90 245 45 235 30 200Z" fill="url(#tipsFill)"/>
    </svg>
  </section>

  <section class="panel panel--inside-middle">
    <p class="kicker">WHAT IS??</p>
    <h2 class="define-title">CIRCADIAN <span>RHYTHM</span><br>DISORDER</h2>
    <p class="text-block define-body">Circadian rhythm disorder is a sleep rhythm disorder. People become this disorder because of the staying up late bad habit or some people has genetic problem and cannot sleep at night but sleepy daytime</p>
    <svg class="art art--sleeper" viewBox="0 0 300 208" role="img" aria-label="Illustration: a person awake in bed under a pink blanket beside a large wall clock and leaves">
      <defs>
        <linearGradient id="sleeperFill" x1="0" y1="0" x2="1" y2="1">
          <stop offset="0" stop-color="#c8cbe6"/>
          <stop offset=".55" stop-color="#e9b0b3"/>
          <stop offset="1" stop-color="#c8cbe6"/>
        </linearGradient>
      </defs>
      <path d="M20 170 C0 120 30 60 80 55 C100 10 200 0 230 40 C280 45 300 110 285 160 C275 200 220 206 150 204 C80 206 35 200 20 170Z" fill="url(#sleeperFill)"/>
    </svg>
    <svg class="clock-icon" viewBox="0 0 58 58" aria-hidden="true">
      <circle cx="29" cy="29" r="26" fill="#fff" stroke="#e8a9ae" stroke-width="3"/>
      <circle cx="29" cy="29" r="20" fill="#fff" stroke="#3f4b7a" stroke-width="1.5"/>
      <g stroke="#3f4b7a" stroke-width="1.2">
        <line x1="29" y1="11" x2="29" y2="14"/><line x1="29" y1="44" x2="29" y2="47"/>
        <line x1="11" y1="29" x2="14" y2="29"/><line x1="44" y1="29" x2="47" y2="29"/>
      </g>
      <line x1="29" y1="29" x2="29" y2="17" stroke="#3f4b7a" stroke-width="1.8" stroke-linecap="round"/>
      <line x1="29" y1="29" x2="38" y2="29" stroke="#3f4b7a" stroke-width="1.8" stroke-linecap="round"/>
      <circle cx="29" cy="29" r="2" fill="#3f4b7a"/>
    </svg>
    <h3 class="subhead">Jet Lag Disorder</h3>
    <p class="text-block jetlag-body">This occurs when a person crosses multiple time zones in a short period of time and gets its name from the fact that it is often experienced by people who take intercontinental flights</p>
    <p class="text-block filler-body">Lorem Ipsum is simply dummy text of the printing and typesetting industry. Lorem Ipsum has been the industry's standard dummy text ever since the 1500s When an unknown printer took a galley of type and scrambled it to make a type specimen book. It has survived not only five centuriesLorem Ipsum has been the industry's standard dummy text ever since the 1500s</p>
  </section>

  <section class="panel panel--cover">
    <h1 class="cover-title">CIRCADIAN<br><span>RHYTHM</span><br>DISORDER</h1>
    <svg class="art art--clock" viewBox="0 0 356 298" role="img" aria-label="Illustration: a clock face split between day and night, framed by a crescent moon, clouds and stars">
      <defs>
        <linearGradient id="coverArtFill" x1="0" y1="0" x2="1" y2="1">
          <stop offset="0" stop-color="#f1c9cc"/>
          <stop offset=".5" stop-color="#c8cbe6"/>
          <stop offset="1" stop-color="#d9dcef"/>
        </linearGradient>
      </defs>
      <path d="M40 230 C0 220 5 150 50 140 C40 80 100 40 150 60 C180 10 270 15 290 70 C345 80 360 160 320 190 C350 240 300 290 240 275 C200 298 120 295 90 270 C60 275 45 255 40 230Z" fill="url(#coverArtFill)"/>
    </svg>
    <svg class="art art--alarm" viewBox="0 0 248 128" role="img" aria-label="Illustration: a digital alarm clock showing 05:00">
      <defs>
        <linearGradient id="alarmFill" x1="0" y1="0" x2="0" y2="1">
          <stop offset="0" stop-color="#e6e1f0"/>
          <stop offset="1" stop-color="#b4bde0"/>
        </linearGradient>
      </defs>
      <rect x="2" y="10" width="244" height="110" rx="24" fill="url(#alarmFill)"/>
    </svg>
  </section>
</div>
</body>
</html>
```